Home page for local retail aggregator

About us: We are a new company that showcases beautiful products available at nearby retail stores. This homepage is meant to display the latest products featured on our site and also allow the user to search, browse with filters, and access their account details.

Currently, our home page looks a little bland. We want the focus of the site to remain on the featured photos and products but the design should be more cohesive. The most successful designs will make more subtle use of our colors, provide intuitive menu controls, and look visually stunning.

This homepage has a few sections:

Header:
-Top Section: will always remain at the top of the page. There should be space for our company name ”zLantern”, a tagline, and a place for the menus.
-Menus: user must be able to find links for: “My profile” “My Products” “Add Product” “Preview store”
-Bottom section: this will scroll with the user and always remain at the top of the screen providing access to a search box, and filters for “location” “price” and retail categories.

Main Page:
-Each product featured is shown on a tile that includes a photo, title, price, name of store, has space to leave a comment, and include counters for "likes," comments, and "Pods"). “Pods” are bookmark folders. The user’s profile pic is also shown in miniature if they leave a comment.

The final version of the site must be delivered in a fully layered photoshop file and have versions demonstrating what the page will look like both when a user is logged-in and when logged-out.

Target Market(s)

Most of our users are female 18-45. Our customers are retail store owners who want their products to look attractive and professional.

Industry/Entity Type

Retail

Requirements
Must have
• Our logo must be present on the site (attached to project). You're welcome to change the colors in the header but it should look good with our logo.

For reference here are colors we're currently using:
Site text is in Dark Blue: RGB(10/23/47)
Logo color on business cards is light blue: (51/153/204)
Nice to have
• Would love to see new versions of the menus that are more modern and intuitive. Currently we just have links to each individual control. Putting these in a drop-down or re-arranging them would be nice.

```html
<!DOCTYPE html>
<html lang="en">
<head>
<meta charset="utf-8">
<title>zLantern – Featured Products</title>
<link href="https://fonts.googleapis.com/css2?family=Alegreya:wght@400;500&family=Open+Sans:wght@400;600;700&family=Playball&display=swap" rel="stylesheet">
<style>
:root{
  --ink:#0a172f;
  --brand:#3399cc;
  --brand-light:#5fb6e6;
  --header:#1f1f20;
  --header-dark:#141415;
  --header-text:#ffffff;
  --wood:#a0582c;
  --wood-light:#b8693a;
  --wood-dark:#8a4623;
  --card:#ffffff;
  --footer:#ececec;
  --tab:#d9d9d9;
  --muted:#6b6b6b;
  --price:#1e5c99;
  --price-dark:#123b66;
  --search-bg:#262627;
  --button:#f5a300;
  --button-dark:#d98a00;
  --nav-sep:#4a4a4a;
}
*{box-sizing:border-box;margin:0;padding:0}
html,body{width:1000px;height:1200px;overflow:hidden}
body{
  position:relative;
  font-family:"Open Sans",Arial,sans-serif;
  color:var(--ink);
  background:linear-gradient(90deg,var(--wood-dark),var(--wood) 20%,var(--wood-light) 45%,var(--wood) 70%,var(--wood-dark));
}
.wood-surface{position:absolute;inset:133px 0 0 0}

/* Header */
.site-header{
  position:absolute;left:0;top:0;width:1000px;height:133px;
  background:linear-gradient(180deg,var(--header) 0%,var(--header-dark) 100%);
}
.color-band{
  position:absolute;left:0;width:100%;height:4px;
  background:repeating-linear-gradient(90deg,#e6367a 0 40px,#f5a300 40px 80px,#ffe14a 80px 120px,#6cc04a 120px 160px,#3399cc 160px 200px,#7b4fc9 200px 240px,#e44b2e 240px 280px);
}
.color-band.top{top:0}
.color-band.bottom{bottom:0}
.brand{position:absolute;left:134px;top:20px;display:flex;align-items:center}
.brand-mark{width:70px;height:70px;border-radius:50%;background:var(--brand);margin-right:28px}
.brand-name{font-family:"Open Sans",Arial,sans-serif;font-weight:400;font-size:24px;color:var(--header-text);margin-top:-10px}
.tagline{position:absolute;left:253px;top:86px;font-family:"Playball",cursive;font-size:22px;color:#fff}
.account{position:absolute;right:108px;top:13px;display:flex;align-items:center;gap:12px}
.account a{font-size:12px;color:#fff;text-decoration:none;letter-spacing:.3px;text-transform:uppercase;padding-right:12px;border-right:1px solid var(--nav-sep)}
.social{width:14px;height:14px;border-radius:50%;background:#e8e8e8}
.main-nav{position:absolute;right:108px;top:96px;display:flex}
.main-nav a{font-size:13.5px;color:#fff;text-decoration:none;padding:0 9px;border-left:1px dotted var(--nav-sep)}
.main-nav a:first-child{border-left:0}
.main-nav a:last-child{padding-right:0}

/* Search */
.search-bar{
  position:absolute;left:207px;top:148px;width:588px;height:52px;
  background:var(--search-bg);border-radius:8px;
  box-shadow:0 2px 4px rgba(0,0,0,.45);
  display:flex;align-items:center;padding-left:18px;gap:8px;
}
.search-label{color:#fff;font-weight:700;font-size:13px;margin-right:2px}
.field{height:23px;background:#fff;border-radius:4px;font-size:11px;color:#555;display:flex;align-items:center;justify-content:space-between;padding:0 9px}
.field.location{width:131px}
.field.select{width:131px}
.field.select svg{width:10px;height:6px}
.search-btn{height:21px;width:78px;border-radius:3px;background:linear-gradient(180deg,#ffc23a,var(--button) 55%,var(--button-dark));color:#fff;font-weight:700;font-size:12px;display:flex;align-items:center;justify-content:center;gap:6px}

/* Grid */
.product-grid{position:absolute;left:112px;top:213px;display:flex;gap:17px}
.column{width:182px;display:flex;flex-direction:column;gap:17px}
.tile{position:relative;background:var(--card);width:182px;padding-top:8px;box-shadow:2px 3px 6px rgba(0,0,0,.35)}
.photo{display:block;width:165px;margin:0 auto}
.title{font-family:"Alegreya",Georgia,serif;font-weight:400;font-size:13.5px;color:var(--ink);padding:0 6px 0 9px;margin-top:12px;line-height:19px;white-space:nowrap;letter-spacing:-.1px}
.meta{position:relative;height:24px;margin-top:5px;padding:0 9px;display:flex;align-items:center}
.store{font-size:9px;color:var(--muted)}
.price{position:absolute;right:-6px;top:-2px;height:24px;min-width:38px;padding:0 8px;background:var(--price);color:#fff;font-family:"Alegreya",Georgia,serif;font-size:12.5px;display:flex;align-items:center;justify-content:center}
.price::after{content:"";position:absolute;right:0;bottom:-5px;border-top:5px solid var(--price-dark);border-right:6px solid transparent}
.counters{display:flex;justify-content:center;gap:5px;margin-top:4px;height:27px}
.counter{width:20px;height:27px;background:var(--tab);clip-path:polygon(0 0,50% 18%,100% 0,100% 100%,0 100%);display:flex;flex-direction:column;align-items:center;justify-content:flex-end;padding-bottom:1px}
.counter svg{width:10px;height:10px}
.counter span{font-size:8px;line-height:10px;color:#444}
.comment{background:var(--footer);height:61px;margin-top:2px;padding:8px 9px 0 9px;display:flex;gap:8px}
.avatar{width:22px;height:22px;background:linear-gradient(160deg,var(--brand-light),var(--brand));border-radius:2px}
.comment-box{flex:1;height:41px;background:#fff;border:1px solid #cfcfcf;font-family:"Alegreya",Georgia,serif;font-size:10.5px;color:#8a8a8a;padding:4px 7px}
</style>
</head>
<body>
<div class="wood-surface" role="img" aria-label="Warm wooden plank background"></div>

<header class="site-header">
  <div class="color-band top"></div>
  <div class="brand">
    <span class="brand-mark"></span>
    <span class="brand-name">zLantern</span>
  </div>
  <div class="tagline">Tagline Goes Here...</div>
  <div class="account">
    <a href="#">+ Join or Login</a>
    <span class="social" aria-label="Social link"></span>
    <span class="social" aria-label="Social link"></span>
    <span class="social" aria-label="Social link"></span>
  </div>
  <nav class="main-nav">
    <a href="#">My Profile</a>
    <a href="#">My Products</a>
    <a href="#">Add Product</a>
    <a href="#">Preview Store</a>
  </nav>
  <div class="color-band bottom"></div>
</header>

<div class="search-bar">
  <span class="search-label">Search:</span>
  <div class="field location">Location</div>
  <div class="field select">Price <svg viewBox="0 0 10 6"><path d="M0 0h10L5 6z" fill="#555"/></svg></div>
  <div class="field select">Retail Categories <svg viewBox="0 0 10 6"><path d="M0 0h10L5 6z" fill="#555"/></svg></div>
  <div class="search-btn">Search <svg width="11" height="11" viewBox="0 0 11 11"><circle cx="4.5" cy="4.5" r="3.3" fill="none" stroke="#5a3a00" stroke-width="1.6"/><path d="M7 7l3 3" stroke="#5a3a00" stroke-width="1.8"/></svg></div>
</div>

<svg width="0" height="0" style="position:absolute">
  <defs>
    <symbol id="i-like" viewBox="0 0 10 10"><circle cx="5" cy="3" r="2.2" fill="#9a9a9a"/><path d="M1 10c0-3 2-4.5 4-4.5s4 1.5 4 4.5z" fill="#9a9a9a"/></symbol>
    <symbol id="i-comment" viewBox="0 0 10 10"><path d="M0 1h10v6H4L1.5 9.5V7H0z" fill="#9a9a9a"/></symbol>
    <symbol id="i-pod" viewBox="0 0 10 10"><path d="M5 0l1.5 3.2 3.5.4-2.6 2.4.7 3.5L5 7.7 1.9 9.5l.7-3.5L0 3.6l3.5-.4z" fill="#9a9a9a"/></symbol>
  </defs>
</svg>

<main class="product-grid">
  <div class="column">
    <article class="tile">
      <div class="photo" style="height:110px;background:linear-gradient(135deg,#d9d6d0,#bfbab2)" role="img" aria-label="Boxed sunflower candle beside a lit glass candle"></div>
      <h3 class="title">Sweet Sunflower Candle</h3>
      <div class="meta"><span class="store">Bramwell</span><span class="price">$30</span></div>
      <div class="counters"><div class="counter"><svg><use href="#i-like"/></svg><span>0</span></div><div class="counter"><svg><use href="#i-comment"/></svg><span>0</span></div><div class="counter"><svg><use href="#i-pod"/></svg><span>0</span></div></div>
      <div class="comment"><div class="avatar" role="img" aria-label="User picture"></div><div class="comment-box">Let the world know...</div></div>
    </article>
    <article class="tile">
      <div class="photo" style="height:110px;background:linear-gradient(180deg,#e2e6e6,#b9bfbf)" role="img" aria-label="Plum pleated fleece hat and scarf on a display head"></div>
      <h3 class="title">Pleated Fleece Scarf</h3>
      <div class="meta"><span class="store">Bramwell</span><span class="price">$60</span></div>
      <div class="counters"><div class="counter"><svg><use href="#i-like"/></svg><span>0</span></div><div class="counter"><svg><use href="#i-comment"/></svg><span>0</span></div><div class="counter"><svg><use href="#i-pod"/></svg><span>0</span></div></div>
      <div class="comment"><div class="avatar" role="img" aria-label="User picture"></div><div class="comment-box">Don't you love this?</div></div>
    </article>
    <article class="tile">
      <div class="photo" style="height:235px;background:linear-gradient(180deg,#7a5a56 0%,#6e6470 45%,#b54a86 75%,#8b5a4c)" role="img" aria-label="Bridal party in grey and pink dresses in front of a brick wall"></div>
      <h3 class="title">Much do</h3>
      <div class="meta"><span class="store">Bramwell</span><span class="price">$58</span></div>
      <div class="counters"><div class="counter"><svg><use href="#i-like"/></svg><span>0</span></div><div class="counter"><svg><use href="#i-comment"/></svg><span>0</span></div><div class="counter"><svg><use href="#i-pod"/></svg><span>0</span></div></div>
      <div class="comment"><div class="avatar" role="img" aria-label="User picture"></div><div class="comment-box">What do you think?</div></div>
    </article>
  </div>

  <div class="column">
    <article class="tile">
      <div class="photo" style="height:245px;background:linear-gradient(160deg,#3a2020,#c98b94 40%,#efe9ea 70%,#c2878e)" role="img" aria-label="White lace-trimmed casual top worn by a model"></div>
      <h3 class="title">Casual top</h3>
      <div class="meta"><span class="store">Maison Perle</span><span class="price">$58</span></div>
      <div class="counters"><div class="counter"><svg><use href="#i-like"/></svg><span>0</span></div><div class="counter"><svg><use href="#i-comment"/></svg><span>0</span></div><div class="counter"><svg><use href="#i-pod"/></svg><span>0</span></div></div>
      <div class="comment"><div class="avatar" role="img" aria-label="User picture"></div><div class="comment-box">What do you think?</div></div>
    </article>
    <article class="tile">
      <div class="photo" style="height:110px;background:linear-gradient(180deg,#9a9a9a,#8c1f30 50%,#b02a3a)" role="img" aria-label="Boxes of red chocolate bars on a shelf"></div>
      <h3 class="title" style="font-size:13px;letter-spacing:-.2px">Emergency Chocolate Rations</h3>
      <div class="meta"><span class="store">Bramwell</span><span class="price">$5</span></div>
      <div class="counters"><div class="counter"><svg><use href="#i-like"/></svg><span>0</span></div><div class="counter"><svg><use href="#i-comment"/></svg><span>0</span></div><div class="counter"><svg><use href="#i-pod"/></svg><span>0</span></div></div>
      <div class="comment"><div class="avatar" role="img" aria-label="User picture"></div><div class="comment-box">Share your thoughts!</div></div>
    </article>
    <article class="tile">
      <div class="photo" style="height:110px;background:linear-gradient(180deg,#d8d8d8,#e9e4dc 55%,#1e1e1e)" role="img" aria-label="Four patterned insulated cups with coloured lids"></div>
      <h3 class="title">Insulated Beverage Holders</h3>
      <div class="meta"><span class="store">Bramwell</span><span class="price">$15</span></div>
      <div class="counters"><div class="counter"><svg><use href="#i-like"/></svg><span>0</span></div><div class="counter"><svg><use href="#i-comment"/></svg><span>0</span></div><div class="counter"><svg><use href="#i-pod"/></svg><span>0</span></div></div>
      <div class="comment"><div class="avatar" role="img" aria-label="User picture"></div><div class="comment-box">Share your thoughts!</div></div>
    </article>
  </div>

  <div class="column">
    <article class="tile">
      <div class="photo" style="height:110px;background:linear-gradient(135deg,#e2e0de,#cbc8c5)" role="img" aria-label="Parrot-shaped corkscrew in blue and orange"></div>
      <h3 class="title">Parrot Corkscrew</h3>
      <div class="meta"><span class="store">Bramwell</span><span class="price">$62</span></div>
      <div class="counters"><div class="counter"><svg><use href="#i-like"/></svg><span>0</span></div><div class="counter"><svg><use href="#i-comment"/></svg><span>0</span></div><div class="counter"><svg><use href="#i-pod"/></svg><span>0</span></div></div>
      <div class="comment"><div class="avatar" role="img" aria-label="User picture"></div><div class="comment-box">What do you think?</div></div>
    </article>
    <article class="tile">
      <div class="photo" style="height:235px;background:linear-gradient(180deg,#7a5a56 0%,#6e6470 45%,#b54a86 75%,#8b5a4c)" role="img" aria-label="Bridal party in grey and pink dresses in front of a brick wall"></div>
      <h3 class="title">Much do</h3>
      <div class="meta"><span class="store">Bramwell</span><span class="price">$58</span></div>
      <div class="counters"><div class="counter"><svg><use href="#i-like"/></svg><span>0</span></div><div class="counter"><svg><use href="#i-comment"/></svg><span>0</span></div><div class="counter"><svg><use href="#i-pod"/></svg><span>0</span></div></div>
      <div class="comment"><div class="avatar" role="img" aria-label="User picture"></div><div class="comment-box">What do you think?</div></div>
    </article>
    <article class="tile">
      <div class="photo" style="height:110px;background:linear-gradient(180deg,#e2e6e6,#b9bfbf)" role="img" aria-label="Plum pleated fleece hat and scarf on a display head"></div>
      <h3 class="title">Pleated Fleece Scarf</h3>
      <div class="meta"><span class="store">Bramwell</span><span class="price">$60</span></div>
      <div class="counters"><div class="counter"><svg><use href="#i-like"/></svg><span>0</span></div><div class="counter"><svg><use href="#i-comment"/></svg><span>0</span></div><div class="counter"><svg><use href="#i-pod"/></svg><span>0</span></div></div>
      <div class="comment"><div class="avatar" role="img" aria-label="User picture"></div><div class="comment-box">Don't you love this?</div></div>
    </article>
  </div>

  <div class="column">
    <article class="tile">
      <div class="photo" style="height:235px;background:linear-gradient(160deg,#b9d6d4,#f4a796 50%,#a9c7c5)" role="img" aria-label="Hand with peach nail polish and one striped accent nail"></div>
      <h3 class="title">Peach nails</h3>
      <div class="meta"><span class="store">Lacquer Lane</span><span class="price">$58</span></div>
      <div class="counters"><div class="counter"><svg><use href="#i-like"/></svg><span>0</span></div><div class="counter"><svg><use href="#i-comment"/></svg><span>0</span></div><div class="counter"><svg><use href="#i-pod"/></svg><span>0</span></div></div>
      <div class="comment"><div class="avatar" role="img" aria-label="User picture"></div><div class="comment-box">What do you think?</div></div>
    </article>
    <article class="tile">
      <div class="photo" style="height:110px;background:linear-gradient(135deg,#e2e0de,#cbc8c5)" role="img" aria-label="Parrot-shaped corkscrew in blue and orange"></div>
      <h3 class="title">Parrot Corkscrew</h3>
      <div class="meta"><span class="store">Bramwell</span><span class="price">$62</span></div>
      <div class="counters"><div class="counter"><svg><use href="#i-like"/></svg><span>0</span></div><div class="counter"><svg><use href="#i-comment"/></svg><span>0</span></div><div class="counter"><svg><use href="#i-pod"/></svg><span>0</span></div></div>
      <div class="comment"><div class="avatar" role="img" aria-label="User picture"></div><div class="comment-box">What do you think?</div></div>
    </article>
    <article class="tile">
      <div class="photo" style="height:110px;background:linear-gradient(135deg,#d9d6d0,#bfbab2)" role="img" aria-label="Boxed sunflower candle beside a lit glass candle"></div>
      <h3 class="title">Sweet Sunflower Candle</h3>
      <div class="meta"><span class="store">Bramwell</span><span class="price">$30</span></div>
      <div class="counters"><div class="counter"><svg><use href="#i-like"/></svg><span>0</span></div><div class="counter"><svg><use href="#i-comment"/></svg><span>0</span></div><div class="counter"><svg><use href="#i-pod"/></svg><span>0</span></div></div>
      <div class="comment"><div class="avatar" role="img" aria-label="User picture"></div><div class="comment-box">Let the world know...</div></div>
    </article>
  </div>
</main>
</body>
</html>
```